Geschäftspapier-Design für Anbieter einer Online-Ausbildung für den qualifizierten Krankentransport und Rettungsdienst
Zielgruppe
LOTH Online-Ausbildung für den qualifizierten Krankentransport und Rettungsdienst
Der qualifizierte Krankentransport und Rettungsdienst ist zuständig für den Transport- und die Versorgung von kranken und verletzten Menschen. LOTH Medizinische Ausbildung und Seminare hat sich als Privatschule für die präklinische Notfallmedizin auf Aus- und Weiterbildungen im E-Learning-Modul für diese zwei Fachbereiche spezialisiert. Alle unsere Fachausbildungen sind online in unserem modernen Campus mit überregionalem Zugang absolvierbar.
Aufgabenstellung
Wir benötigen eine Word-Briefvorlage für den alltäglichen Geschäftsverkehr in drei Ausführungen.
- Briefvorlage mit Angabe der Abteilung -> Sekretariat
- Briefvorlage mit Angabe der Abteilung -> Schulleitung
- Briefvorlage mit Angabe der Abteilung -> Geschäftsführung
- Briefvorlage mit Angabe der Abteilung -> Buchhaltung/ Forderungsmanagement
Die Vorlage sollte bitte folgende Angaben aufweisen:
LOTH Bildungsgesellschaft UG (haftungsbeschränkt)
Privatschule für prähospitale Rettungsmedizin
Standort unserer Verwaltung:
Farnhügel 7
15537 Erkner
Standort unseres Schulsitzes:
Am Quendelhof 48
D- 15537 Gosen- Neu Zittau
Schulleitung: Jutta Wildgrube & Matthias Lot
Ärztliche Leitung: Dr. Med. Ortwin Brasch
Pädagogische Leitung: Matthias Loth
Fachlicher Beirat: Dr. rer. med. Fabian Oswalt
Tel: 030 6270384 50
Fax: 030 6270384 51
E-Mail: info@loth-lehrwerkstatt.de
Web: www.loth-lehrwerkstatt.de
Vertreten durch: Jutta Wildgrube
Registereintrag: Eintragung im Handelsregister Registergericht: Amtsgericht Frankfurt (Oder) Registernummer: HRB 27403 FF

```html
<!DOCTYPE html>
<html lang="de">
<head>
<meta charset="utf-8">
<title>LOTH Bildungsgesellschaft – Briefbogen Geschäftsführung</title>
<link href="https://fonts.googleapis.com/css2?family=Source+Sans+3:wght@400;600;700&display=swap" rel="stylesheet">
<style>
  :root {
    --brand-blue: #6aa6d6;
    --ink: #1d1d1b;
    --paper: #ffffff;
  }
  * { margin: 0; padding: 0; box-sizing: border-box; }
  html, body { width: 862px; height: 1200px; overflow: hidden; background: var(--paper); }
  body { position: relative; font-family: "Source Sans 3", "Myriad Pro", sans-serif; color: var(--ink); }

  .sheet-frame { position: absolute; left: 37px; top: 43px; width: 788px; height: 1113px; border: 1px solid var(--ink); }
  .side-band { position: absolute; left: 37px; top: 43px; width: 19px; height: 1113px; background: var(--brand-blue); }
  .side-band .gap { position: absolute; left: 0; width: 19px; height: 2px; background: var(--paper); }
  .edge-tab { position: absolute; left: 815px; width: 9px; background: var(--brand-blue); }
  .edge-tab.upper { top: 228px; height: 152px; }
  .edge-tab.lower { top: 975px; height: 180px; }

  .letterhead { position: absolute; right: 187px; top: 92px; text-align: right; font-weight: 600; font-size: 12.5px; line-height: 16.5px; }
  .letterhead .tagline { margin-top: 4px; }
  .head-divider { position: absolute; left: 693px; top: 69px; width: 1px; height: 112px; background: var(--ink); }
  .brand-mark { position: absolute; left: 711px; top: 100px; display: flex; align-items: center; gap: 7px; }
  .brand-mark .square { width: 14px; height: 14px; background: var(--brand-blue); }
  .brand-mark .name { font-weight: 700; font-size: 30px; color: var(--brand-blue); letter-spacing: 1px; }

  .return-address { position: absolute; left: 139px; top: 220px; width: 262px; font-size: 9px; line-height: 12px; border-bottom: 1px solid var(--ink); padding-bottom: 1px; white-space: nowrap; }
  .fold-mark { position: absolute; top: 386px; width: 2px; height: 2px; background: var(--ink); border-radius: 50%; }

  .contact-block { position: absolute; right: 69px; top: 228px; text-align: right; font-size: 10.5px; line-height: 14px; white-space: nowrap; }
  .contact-block .department { font-weight: 700; font-size: 13px; color: var(--brand-blue); margin-bottom: 7px; }
  .contact-block .label { color: var(--brand-blue); }
  .contact-block .group { margin-top: 3px; }

  .company-info { position: absolute; right: 69px; top: 982px; text-align: right; font-size: 8.3px; line-height: 12px; white-space: nowrap; }
  .company-info .label { color: var(--brand-blue); font-weight: 600; }
  .company-info .group + .group { margin-top: 6px; }
</style>
</head>
<body>
  <div class="sheet-frame"></div>
  <div class="side-band">
    <span class="gap" style="top:391px"></span>
    <span class="gap" style="top:555px"></span>
  </div>
  <div class="edge-tab upper"></div>
  <div class="edge-tab lower"></div>

  <header class="letterhead">
    <p>LOTH Bildungsgesellschaft UG</p>
    <p>(haftungsbeschränkt)</p>
    <p class="tagline">Privatschule für</p>
    <p>prähospitale Rettungsmedizin</p>
  </header>
  <div class="head-divider"></div>
  <div class="brand-mark">
    <span class="square"></span>
    <span class="name">LOTH</span>
  </div>

  <p class="return-address">LOTH Bildungsgesellschaft UG &nbsp;|&nbsp; Farnhügel 7 &nbsp;|&nbsp; 15537 Erkner</p>
  <span class="fold-mark" style="left:111px"></span>
  <span class="fold-mark" style="left:429px"></span>

  <aside class="contact-block">
    <p class="department">– Geschäftsführung –</p>
    <p class="label">Verwaltung:</p>
    <p>Farnhügel 7 · 15537 Erkner</p>
    <p class="label group">Schulsitz:</p>
    <p>Am Quendelhof 48 · 15537 Gosen-Neu Zittau</p>
    <p class="group">Tel. 030&nbsp; 6270384 50</p>
    <p>Fax 030&nbsp; 6270384 51</p>
    <p class="group">E-Mail: info@loth-lehrwerkstatt.de</p>
    <p>Web: www.loth-lehrwerkstatt.de</p>
  </aside>

  <footer class="company-info">
    <div class="group">
      <p><span class="label">Schulleitung:</span> Jutta Wildgrube · Matthias Loth</p>
      <p><span class="label">Ärztliche Leitung:</span> Dr. med. Ortwin Brasch</p>
      <p><span class="label">Pädagogische Leitung:</span> Matthias Loth</p>
      <p><span class="label">Fachlicher Beirat:</span> Dr. rer. med. Fabian Oswalt</p>
    </div>
    <div class="group">
      <p><span class="label">Vertreten durch:</span> Jutta Wildgrube</p>
      <p><span class="label">Registereintrag:</span> Eintragung im Handelsregister</p>
      <p><span class="label">Registergericht:</span> Amtsgericht Frankfurt (Oder)</p>
      <p><span class="label">Registernummer:</span> HRB 27403 FF</p>
    </div>
    <div class="group">
      <p class="label">Kontoverbindung:</p>
      <p>Spreetaler Sparkasse</p>
      <p>IBAN: DE00 0000 0000 0000 0000 00</p>
      <p>BIC: XXXXXXXXXXX</p>
    </div>
  </footer>
</body>
</html>
```